VTM letterhead

We need the Letterhead and a page 2 which will be a simpler page - less header space for the design. Use the design you just created for the Business card. Be sure Page 2 allows for a full page of content.

Industry/Entity Type

Business

```html
<!DOCTYPE html>
<html lang="en">
<head>
<meta charset="utf-8">
<title>VTM Letterhead</title>
<link rel="stylesheet" href="https://fonts.googleapis.com/css2?family=Lato:wght@400;700;900&display=swap">
<style>
  :root {
    --bg: #e6e6e6;
    --paper: #ffffff;
    --ink: #1a1a1a;
    --brand-red: #c1202b;
    --brand-black: #111111;
    --rule: #cfcfcf;
    --muted: #444444;
  }
  * { margin: 0; padding: 0; box-sizing: border-box; }
  html, body {
    width: 1200px; height: 799px; overflow: hidden;
    background: var(--bg);
    font-family: "Lato", Arial, sans-serif;
    color: var(--ink);
  }
  .canvas { position: relative; width: 1200px; height: 799px; }
  .sheet {
    position: absolute; top: 82px;
    width: 462px; height: 646px;
    background: var(--paper);
    overflow: hidden;
  }
  .sheet--first { left: 90px; }
  .sheet--body { left: 666px; overflow: visible; }
  .sheet__top, .sheet__bottom { position: absolute; left: 0; width: 462px; }
  .sheet__top { top: 0; height: 14px; }
  .sheet__bottom { bottom: 0; height: 30px; }
  .brand {
    position: absolute; top: 18px; left: 0; width: 100%;
    text-align: center;
    font-weight: 900; font-size: 30px; letter-spacing: 1px;
    color: var(--brand-red); line-height: 1;
  }
  .address {
    position: absolute; top: 52px; left: 0; width: 100%;
    text-align: center; font-size: 8px; letter-spacing: 0.3px; color: var(--muted);
  }
  .header-rule {
    position: absolute; top: 68px; left: 40px; width: 380px;
    height: 1px; background: var(--rule);
  }
  .contact {
    position: absolute; top: 598px; left: 0; width: 100%;
    text-align: center; font-size: 7.5px; color: var(--muted); white-space: nowrap;
  }
  .contact .label { color: var(--brand-red); font-weight: 700; }
  .contact span + span { margin-left: 7px; }
  .tagline {
    position: absolute; bottom: 8px; left: 0; width: 100%;
    text-align: center; color: #fff; font-size: 8px; font-weight: 700;
  }
  .letter {
    position: absolute; top: 140px; left: 52px; width: 360px;
    font-size: 9px; line-height: 11.2px; color: var(--ink);
  }
  .letter p { margin-bottom: 11px; }
  .letter .salutation { margin-bottom: 11px; }
  .letter .salutation strong { font-weight: 700; }
  .accent-bar {
    position: absolute; left: -6px; top: 443px; width: 11px; height: 64px;
    background: var(--brand-red);
  }
  .signature {
    position: absolute; left: 52px; top: 446px; width: 110px; height: 22px;
    background: linear-gradient(90deg, #eeeeee, #f6f6f6);
  }
  .signer { position: absolute; left: 52px; top: 480px; }
  .signer__name { font-size: 11px; font-weight: 400; }
  .signer__name strong { font-weight: 900; }
  .signer__title {
    font-size: 7.5px; font-weight: 700; letter-spacing: 1px; color: var(--brand-red);
  }
</style>
</head>
<body>
<div class="canvas">

  <section class="sheet sheet--first" aria-label="Letterhead first page">
    <svg class="sheet__top" viewBox="0 0 462 14" preserveAspectRatio="none" aria-hidden="true">
      <path d="M0 0 H462 V2 Q231 26 0 2 Z" fill="var(--brand-black)"/>
    </svg>
    <div class="brand">VTM</div>
    <div class="address">2750 Meridian Avenue, Suite 210, Fairview, MD 20900</div>
    <div class="header-rule"></div>
    <div class="contact">
      <span><b class="label">O:</b> 240.555.0142</span>
      <span><b class="label">F:</b> 240.555.0187</span>
      <span><b class="label">C:</b> 703.555.0163</span>
      <span><b class="label">E:</b> dana@vtmtechgroup.com</span>
      <span><b class="label">W:</b> www.vtmtechgroup.com</span>
    </div>
    <svg class="sheet__bottom" viewBox="0 0 462 30" preserveAspectRatio="none" aria-hidden="true">
      <path d="M0 30 V14 Q231 -10 462 14 V30 Z" fill="var(--brand-red)"/>
    </svg>
    <div class="tagline">Woman Owned Small Business</div>
  </section>

  <section class="sheet sheet--body" aria-label="Letterhead with sample letter">
    <svg class="sheet__top" viewBox="0 0 462 14" preserveAspectRatio="none" aria-hidden="true">
      <path d="M0 0 H462 V2 Q231 26 0 2 Z" fill="var(--brand-black)"/>
    </svg>
    <div class="brand">VTM</div>
    <div class="address">2750 Meridian Avenue, Suite 210, Fairview, MD 20900</div>
    <div class="header-rule"></div>

    <article class="letter">
      <div class="salutation">Lorem<br><strong>ipsum dolor sit amet</strong>,</div>
      <p>consectetur adipiscing elit. Duis facilisis elementum dui, bibendum pulvinar nulla malesuada quis. Curabitur ut leo quam. Pellentesque laoreet metus risus, non fermentum arcu malesuada vitae. Vestibulum dui libero, vestibulum non quam sit amet, auctor lobortis tortor. Integer blandit enim vitae adipiscing adipiscing. Vivamus metus lacus, porta at aliquam sit amet,</p>
      <p>pretium ut eros. Curabitur a dui interdum, elementum urna ut, venenatis erat. Fusce feugiat odio sed dui rhoncus auctor. Aenean posuere, odio ut facilisis tempus, nunc mauris convallis lacus, eget vulputate enim purus ac odio. Donec blandit et ipsum a aliquet. Mauris semper diam in velit vestibulum, sit amet molestie purus convallis. Duis pulvinar porttitor magna in malesuada.</p>
      <p>Nullam auctor neque orci, nec ornare odio auctor et. Phasellus eu sapien nec nibh lobortis commodo. Donec nec commodo nibh. Sed nec nulla et magna fermentum suscipit. Nam ligula nunc, facilisis iaculis venenatis eget,</p>
      <p>gravida consectetur odio. Donec in leo ac felis vestibulum feugiat. In at orci id justo adipiscing vehicula. Sed tortor purus, pellentesque vel lobortis nec, tincidunt vitae mi. Duis pellentesque augue vitae pharetra euismod.</p>
      <p>Duis vulputate, libero nec vehicula pretium, mi nisi tristique mauris, ac porttitor diam metus at ante. Pellentesque magna arcu, viverra ac lacinia nec, pharetra id est. Maecenas ullamcorper mattis tellus, et dapibus arcu sagittis malesuada.</p>
    </article>

    <div class="accent-bar"></div>
    <div class="signature" role="img" aria-label="Handwritten signature of Dana Whitfield"></div>
    <div class="signer">
      <div class="signer__name">Dana <strong>Whitfield</strong></div>
      <div class="signer__title">PRESIDENT</div>
    </div>

    <div class="contact">
      <span><b class="label">O:</b> 240.555.0142</span>
      <span><b class="label">F:</b> 240.555.0187</span>
      <span><b class="label">C:</b> 703.555.0163</span>
      <span><b class="label">E:</b> dana@vtmtechgroup.com</span>
      <span><b class="label">W:</b> www.vtmtechgroup.com</span>
    </div>
    <svg class="sheet__bottom" viewBox="0 0 462 30" preserveAspectRatio="none" aria-hidden="true">
      <path d="M0 30 V14 Q231 -10 462 14 V30 Z" fill="var(--brand-red)"/>
    </svg>
    <div class="tagline">Woman Owned Small Business</div>
  </section>

</div>
</body>
</html>
```